Craft brewery keg badge / badge branding to be on display on keg fonts in pubs and craft beer bars

We're a small craft beer producer and are looking to have a keg badge designed to be put onto keg fonts in bars as well as being used on our bottles. Our website is www.qelmarbrewing.co.uk. -Please take a look at our site however we're looking for new branding! We're not looking to have the windmill on the badge! We want a bold geometric hop design in the centre of the design. The beer is a low AVB beer (2.9% ABV) and will be hopped with Cascade, Colombus and Mosaic hops and will have a fruity / juicy aroma. We're looking to have a design that we can re-use again and again by changing: colours and wording for different beers in the future.

Target Market(s)
Craft beer drinkers
Industry/Entity Type
Craft Brewery
Requirements
Must have
- Simple, elegant, repeatable core message from the badge. It need a simple, bold geometric hop design (examples uploaded) in the centre which is repeatable across many brands in the future.
- The badge needs to be circular and 82mm across to fit our tap lenses (see http://www.drevix.co.uk/branding for the flat lens). The keg badge needs to be modern and in line with other keg badges like the examples attached- though we leave the artistic flair up to you guys. Please see below the styles of keg badge we like.
- Must be in vector file format and we must get a jpeg version too.

Should not have
- Should not be overcrowded and try to be too full of information. See attached examples.

```html
<!DOCTYPE html>
<html lang="en">
<head>
<meta charset="utf-8">
<title>Qelmar Brewing – Keg Badges</title>
<link rel="stylesheet" href="https://fonts.googleapis.com/css2?family=Oswald:wght@600&display=swap">
<style>
  :root {
    --paper: #ffffff;
    --ink-red: #ea3d33;
    --ink-black: #0a0a0a;
    --teal: #12b3a6;
    --navy: #2a3a92;
    --purple: #6a2f96;
    --brown: #774b27;
    --orange: #f06a22;
  }
  html, body {
    margin: 0;
    padding: 0;
    width: 1200px;
    height: 1200px;
    overflow: hidden;
    background: var(--paper);
  }
  .canvas {
    display: block;
    width: 1200px;
    height: 1200px;
  }
  .badge-name {
    font-family: "Oswald", "Arial Narrow", sans-serif;
    font-weight: 600;
    font-size: 40px;
    letter-spacing: 1px;
    text-anchor: middle;
  }
  .badge-name--red { fill: var(--ink-red); }
  .badge-name--black { fill: var(--ink-black); }
  .brand-mark {
    font-family: "Oswald", "Arial Narrow", sans-serif;
    font-weight: 600;
    font-size: 30px;
    fill: var(--paper);
    text-anchor: middle;
  }
  .brand-dot { fill: var(--paper); }
  .label-panel { fill: var(--paper); }
</style>
</head>
<body>
<svg class="canvas" viewBox="0 0 1200 1200" xmlns="http://www.w3.org/2000/svg">
  <defs>
    <linearGradient id="mosaic-warm" x1="0" y1="0" x2="1" y2="1">
      <stop offset="0" stop-color="#774b27"/>
      <stop offset="0.3" stop-color="#ea3d33"/>
      <stop offset="0.55" stop-color="#6a2f96"/>
      <stop offset="0.8" stop-color="#2a3a92"/>
      <stop offset="1" stop-color="#12b3a6"/>
    </linearGradient>
    <linearGradient id="mosaic-dark" x1="0" y1="0" x2="1" y2="1">
      <stop offset="0" stop-color="#f06a22"/>
      <stop offset="0.3" stop-color="#6a2f96"/>
      <stop offset="0.6" stop-color="#2a3a92"/>
      <stop offset="1" stop-color="#12b3a6"/>
    </linearGradient>
    <clipPath id="label-red-clip"><circle cx="373" cy="390" r="283"/></clipPath>
    <clipPath id="label-black-clip"><circle cx="830" cy="823" r="286"/></clipPath>
  </defs>

  <!-- Badge: red lead-line edition -->
  <g class="badge badge--red">
    <circle class="badge-mosaic" cx="373" cy="390" r="296" fill="url(#mosaic-warm)"
            role="img" aria-label="Geometric stained-glass mosaic in red, brown, purple, navy and teal"/>
    <rect class="label-panel" x="60" y="472" width="640" height="260" clip-path="url(#label-red-clip)"/>
    <g class="brand-lockup">
      <circle class="brand-dot" cx="373" cy="292" r="12"/>
      <text class="brand-mark" x="373" y="345">QELMAR</text>
    </g>
    <text class="badge-name badge-name--red" x="373" y="576">QELMARBREWING</text>
  </g>

  <!-- Badge: black lead-line edition -->
  <g class="badge badge--black">
    <circle class="badge-mosaic" cx="830" cy="823" r="298" fill="url(#mosaic-dark)"
            role="img" aria-label="Geometric stained-glass mosaic in orange, purple, navy and teal with black lead lines"/>
    <rect class="label-panel" x="520" y="912" width="640" height="260" clip-path="url(#label-black-clip)"/>
    <g class="brand-lockup">
      <circle class="brand-dot" cx="824" cy="722" r="12"/>
      <text class="brand-mark" x="824" y="775">QELMAR</text>
    </g>
    <text class="badge-name badge-name--black" x="830" y="1015">QELMARBREWING</text>
  </g>
</svg>
</body>
</html>
```